Business Cards

I'd like help creating business cards with the full logo "Veltrona Capital Partners" on the back of the card (navy background with white writing), and abbreviated logo "VCP" on the front. Would like to list name, title, phone number, email, and website listed on front of card. Would like to keep very simple. Front font Arial or similar.

```html
<!DOCTYPE html>
<html lang="en">
<head>
<meta charset="utf-8">
<title>Veltrona Capital Partners – Business Cards</title>
<link rel="stylesheet" href="https://fonts.googleapis.com/css2?family=Arimo:wght@400;700&family=Montserrat:wght@600;800&display=swap">
<style>
  :root {
    --stage: #2b2b2b;
    --navy: #1b3a6e;
    --navy-deep: #14305c;
    --navy-soft: #2a4c86;
    --white: #ffffff;
    --ink: #1c3b72;
  }
  * { box-sizing: border-box; margin: 0; padding: 0; }
  html, body { width: 1200px; height: 689px; overflow: hidden; }
  body {
    background: var(--stage);
    display: flex;
    align-items: center;
    justify-content: center;
    gap: 60px;
  }
  .card {
    width: 525px;
    height: 300px;
    border-radius: 22px;
    position: relative;
    overflow: hidden;
    box-shadow: 0 12px 30px rgba(0,0,0,0.45);
  }

  /* Back: navy with full company name */
  .card-back { background: var(--navy); }
  .card-back .backdrop {
    position: absolute; inset: 0;
    background: linear-gradient(135deg, var(--navy-soft) 0%, var(--navy) 50%, var(--navy-deep) 100%);
  }
  .card-back .wordmark {
    position: absolute;
    left: 0; right: 0; top: 50%;
    transform: translateY(-50%);
    text-align: center;
    color: var(--white);
    font-family: "Montserrat", sans-serif;
  }
  .wordmark .name {
    display: block;
    font-weight: 800;
    font-size: 52px;
    letter-spacing: 1px;
    line-height: 1;
  }
  .wordmark .sub {
    display: block;
    margin-top: 12px;
    font-weight: 600;
    font-size: 17px;
    letter-spacing: 9px;
  }

  /* Front: initials and contact details */
  .card-front {
    background: var(--white);
    display: flex;
    align-items: center;
    padding: 0 36px 0 44px;
    font-family: "Arimo", sans-serif;
    color: var(--ink);
  }
  .initials {
    font-weight: 700;
    font-size: 74px;
    letter-spacing: 2px;
    color: var(--ink);
    width: 190px;
  }
  .divider {
    width: 1.5px;
    height: 120px;
    background: var(--ink);
    margin: 0 26px 0 14px;
  }
  .details .person {
    font-weight: 700;
    font-size: 21px;
    letter-spacing: 0.5px;
    text-transform: uppercase;
  }
  .details .role {
    font-size: 14px;
    margin-top: 3px;
  }
  .contacts {
    list-style: none;
    margin-top: 16px;
    font-size: 13px;
  }
  .contacts li {
    display: flex;
    align-items: center;
    gap: 7px;
    line-height: 1.55;
  }
  .contacts svg { width: 12px; height: 12px; fill: var(--ink); flex: none; }
</style>
</head>
<body>

  <section class="card card-back" aria-label="Card back">
    <div class="backdrop" role="img" aria-label="Navy background with faint repeated company initials pattern"></div>
    <div class="wordmark">
      <span class="name">VELTRONA</span>
      <span class="sub">CAPITAL PARTNERS</span>
    </div>
  </section>

  <section class="card card-front" aria-label="Card front">
    <div class="initials">VCP</div>
    <div class="divider"></div>
    <div class="details">
      <div class="person">Dorian Vale</div>
      <div class="role">Managing Director</div>
      <ul class="contacts">
        <li>
          <svg viewBox="0 0 24 24" aria-hidden="true"><path d="M6.6 10.8a15.1 15.1 0 0 0 6.6 6.6l2.2-2.2a1 1 0 0 1 1-.25 11.4 11.4 0 0 0 3.6.57 1 1 0 0 1 1 1V20a1 1 0 0 1-1 1A17 17 0 0 1 3 4a1 1 0 0 1 1-1h3.5a1 1 0 0 1 1 1c0 1.25.2 2.45.57 3.57a1 1 0 0 1-.25 1z"/></svg>
          044-555 010 246
        </li>
        <li>
          <svg viewBox="0 0 24 24" aria-hidden="true"><path d="M2 5h20v14H2z M2 5l10 8 10-8" fill="none" stroke="#1c3b72" stroke-width="2"/><path d="M2 5h20l-10 8z"/></svg>
          info@veltrona-cp.com
        </li>
        <li>
          <svg viewBox="0 0 24 24" aria-hidden="true"><circle cx="12" cy="12" r="9" fill="none" stroke="#1c3b72" stroke-width="2"/><path d="M3 12h18M12 3c3 3 3 15 0 18M12 3c-3 3-3 15 0 18" fill="none" stroke="#1c3b72" stroke-width="1.6"/></svg>
          www.veltrona-cp.com
        </li>
      </ul>
    </div>
  </section>

</body>
</html>
```